Yacht, Boats, Watersports company needs a redesign of business card

Hello Designers!
We are a Boat dealership company that sells fun in the water, we sell boats, Yachts, Kayaks and also yacht WaterSport toys. We are looking to redesign our business cards in to something a little bit more sophisticated. in a way that we can make better use of our company colors. I'm attaching a zipped file containing the company 3 sets of company logo which one is an horizontal another one is a vertical and also a chromed 3d logo. Also is included two set of business cards that we use and also some designs that i think it's interesting. We use PMS 2026c Orange and PMS 7687C Blue. I would like to see at least two different options with the orange as accent and also using blue as an accent color. It's really important for the business cards to have a font option and size that is legible to most people. Our current website is wwww.corvellamarine.com. Please visit if you want to have a better feeling of the Boat dealership
You can send Single sided or double side options. We are now using single sided but we may be open for a double side option if we really like the design.
Target Market(s)
Marine, boat sales, yacht sales, water toys sales/
Contact Information for Business Card
Name: Dale Pritchett
Address: 718 West Halden Lane,
Marlow Springs, FL 30519
Phone: 555-382-7146
Fax: 954:382-7139
Cell: 555-451-8320
Email: 212@corvellamarine.com
Website: corvellamarine.com
Requirements
Must have
- the current information of the business card provided.
logo
use the PMS Colors
Nice to have
- a touch of elegance and sophistication but simple
Should not have
- should not have any typography that is hard to read, the card should be simple but yet sophisticated.

```html
<!DOCTYPE html>
<html lang="en">
<head>
<meta charset="utf-8">
<title>Corvella Marine — Business Card</title>
<link rel="stylesheet" href="https://fonts.googleapis.com/css2?family=Poppins:wght@400;600;700&display=swap">
<style>
  :root {
    --bg: #e6e6e8;
    --blue: #1562b3;
    --blue-deep: #0f57a6;
    --orange: #f07d1a;
    --white: #ffffff;
  }
  * { margin: 0; padding: 0; box-sizing: border-box; }
  html, body { width: 1200px; height: 800px; overflow: hidden; }
  body {
    background: var(--bg);
    font-family: "Poppins", sans-serif;
    display: flex;
    align-items: center;
    justify-content: center;
    gap: 40px;
  }
  .card {
    width: 540px;
    height: 309px;
    border-radius: 24px;
    background: linear-gradient(160deg, var(--blue), var(--blue-deep));
    box-shadow: 0 3px 0 var(--orange), 0 14px 30px rgba(0,0,0,0.18);
    position: relative;
    overflow: hidden;
  }
  /* Contact side */
  .card--contact { display: flex; align-items: center; }
  .holder-name {
    width: 232px;
    text-align: center;
    color: var(--orange);
    font-weight: 600;
    font-size: 21px;
    letter-spacing: 0.5px;
    text-transform: uppercase;
  }
  .divider {
    width: 2px;
    height: 150px;
    background: var(--orange);
  }
  .contact-list {
    list-style: none;
    padding-left: 26px;
    color: var(--white);
    font-size: 13px;
    line-height: 1.38;
  }
  .contact-list li { display: flex; align-items: flex-start; gap: 9px; }
  .contact-list li.address { margin-bottom: 10px; }
  .contact-list svg { flex: 0 0 12px; width: 12px; height: 12px; margin-top: 3px; fill: var(--orange); }
  /* Brand side */
  .card--brand {
    display: flex;
    flex-direction: column;
    align-items: center;
    justify-content: center;
    gap: 18px;
  }
  .brand-mark {
    width: 64px; height: 64px;
    border: 6px solid var(--orange);
    border-radius: 50%;
  }
  .brand-name {
    color: var(--white);
    font-weight: 700;
    font-size: 34px;
    letter-spacing: 1px;
    text-transform: uppercase;
  }
</style>
</head>
<body>

<section class="card card--contact" aria-label="Business card contact side">
  <h1 class="holder-name">Dale Pritchett</h1>
  <div class="divider"></div>
  <ul class="contact-list">
    <li class="address">
      <svg viewBox="0 0 12 12"><path d="M6 0a4 4 0 0 0-4 4c0 3 4 8 4 8s4-5 4-8a4 4 0 0 0-4-4zm0 5.6A1.6 1.6 0 1 1 6 2.4a1.6 1.6 0 0 1 0 3.2z"/></svg>
      <span>718 West Halden Lane,<br>Marlow Springs, FL 30519</span>
    </li>
    <li>
      <svg viewBox="0 0 12 12"><path d="M2.4 0.5l2 2.2-1 1.4a7 7 0 0 0 4.5 4.5l1.4-1 2.2 2-1.3 1.8C5 11 1 7 0.6 1.8z"/></svg>
      <span>555-382-7146</span>
    </li>
    <li>
      <svg viewBox="0 0 12 12"><path d="M1 1h10v10H1zm1.5 1.5v7h7v-7z"/></svg>
      <span>555-451-8320</span>
    </li>
    <li>
      <svg viewBox="0 0 12 12"><path d="M3 0h6v12H3zm1.2 1.3v8h3.6v-8z"/></svg>
      <span>555:382-7139</span>
    </li>
    <li>
      <svg viewBox="0 0 12 12"><path d="M0 2h12v8H0zm1.2 1.2L6 6.6l4.8-3.4z"/></svg>
      <span>212@corvellamarine.com</span>
    </li>
    <li>
      <svg viewBox="0 0 12 12"><circle cx="6" cy="6" r="6"/><path d="M0 6h12M6 0v12" stroke="#1562b3" stroke-width="1"/></svg>
      <span>corvellamarine.com</span>
    </li>
  </ul>
</section>

<section class="card card--brand" aria-label="Business card brand side">
  <div class="brand-mark"></div>
  <p class="brand-name">Corvella Marine</p>
</section>

</body>
</html>
```